Postcard Campaign for Real Estate Company

Project Goal: Our goal through this project is to locate a designer with whom we can work on a long term basis.
As a way to do that, we’ve created this Pixel Bazaar project. For this project, we would like you to
design 4 postcards that would be part of that mailing campaign. We’d like each to be unique and yet
also have cohesiveness in our brand – so we can see how you would present 3 or 4 different kinds of
information about us.
We use a postcard mailing campaigns (a) to stay in touch with past clients and (b) to send to “geographic
farms” – areas where we want to establish our brand and gain leads and business.
For this project, we are providing our logo, contact information, and statistics/information we want on
the postcards. We are also attaching past postcards we have sent out for examples - HOWEVER, we are
looking to ELEVATE our postcards and make them MORE COHESIVE.
Postcard 1: Highlighting the Harbor Crest award that we just received again in 2022 – for the 2 nd
years. We want to include the provided statistics; we've also attached our previous postcard for this
award but want to elevate the look.
Link to statistics: https://www.homeledgerpro.com/harbor-crest/
Postcard 2: A side-by-side comparison of a property we sold and a property another agent sold in the
same building where our stats are far superior. For a similar idea, see the PLONK postcard we’ve
attached.
The property we sold is 42 Palmer Ave, Unit 718, Cambridge (2 bedroom, 2 bathroom, 1327 square feet, 8
days on market, list price $1,189,000, sale price $1,300,000, sale to list ratio 109%).
The property we want to compare it to is 42 Palmer Ave, Unit 706 Cambridge (2 bedrooms, 2 bathrooms,
1277 square feet, 74 days on market, list price $1,195,000, sale price $1,180,000, sale to list ratio 99%)
.If you'd like, or have room on the postcard, to compare another property, use 42 Palmer Ave, Unit 404,
Cambridge (2 bedroom, 2 bathroom, 1369 square feet, 25 days on market, list price $1,250,000, sale
price $1,200,000, sale to list price ratio 96%).
The goal is to highlight our services and expertise in getting the highest price and fast results.
Postcards 3 and 4: These will be infographics, using the data provided (see files: Infographic Info
Postcard 1 and 2, along with the credits and Infographic Postcard 1 Backside). You can choose the
graphics you like from things in public domain or things you create. The attachments we are provided
are from an email blast we received from a mortgage lender.
We'd like these infographics postcards to have the feel a part of our brand and also provide data in an
eye-catching way.
We are looking forward to how you want to present us and this to our audience! Thank you!!

```html
<!DOCTYPE html>
<html lang="en">
<head>
<meta charset="utf-8">
<title>Postcard 2 : Comparison</title>
<link href="https://fonts.googleapis.com/css2?family=Arimo:wght@400;700&display=swap" rel="stylesheet">
<style>
  :root {
    --red: #f20f0f;
    --black: #000;
    --white: #fff;
    --grey: #7d7d7d;
    --rule: #9a9a9a;
    --divider: #cfcfcf;
    --page: #fff;
  }
  * { box-sizing: border-box; margin: 0; padding: 0; }
  html, body { width: 1200px; height: 900px; overflow: hidden; background: var(--page); }
  body { position: relative; font-family: "Arimo", Arial, sans-serif; }

  .sheet-title {
    position: absolute; left: 0; top: 98px; width: 1200px;
    text-align: center; color: var(--red);
    font-size: 35px; font-weight: 700; letter-spacing: 3px;
  }

  .postcard {
    position: absolute; left: 218px; top: 205px; width: 770px; height: 496px;
    border: 1px solid #222; overflow: hidden; background: var(--divider);
  }

  .photo { position: absolute; }
  .photo--feature {
    left: 0; top: 0; width: 381px; height: 494px;
    background:
      radial-gradient(ellipse 38% 18% at 72% 40%, rgba(250,252,250,0.95) 0%, rgba(240,244,240,0) 100%),
      radial-gradient(ellipse 20% 14% at 45% 30%, rgba(176,110,92,0.55) 0%, rgba(176,110,92,0) 100%),
      radial-gradient(ellipse 28% 10% at 70% 46%, rgba(92,140,80,0.65) 0%, rgba(92,140,80,0) 100%),
      radial-gradient(ellipse 55% 16% at 55% 64%, rgba(150,152,160,0.9) 0%, rgba(150,152,160,0) 100%),
      radial-gradient(ellipse 22% 10% at 80% 74%, rgba(40,44,48,0.55) 0%, rgba(40,44,48,0) 100%),
      linear-gradient(90deg, rgba(120,120,120,0.35) 0%, rgba(120,120,120,0) 22%),
      linear-gradient(180deg, #cfcfcf 0%, #e6e6e4 25%, #e9ebe8 45%, #c7c8cc 62%, #a5a6aa 78%, #5d5d5d 100%);
  }
  .photo--unit404 {
    left: 389px; top: 0; width: 380px; height: 244px;
    background:
      radial-gradient(ellipse 22% 22% at 50% 28%, rgba(236,242,236,1) 0%, rgba(236,242,236,0) 100%),
      radial-gradient(ellipse 14% 16% at 48% 36%, rgba(100,140,96,0.6) 0%, rgba(100,140,96,0) 100%),
      radial-gradient(ellipse 16% 40% at 93% 40%, rgba(150,80,62,0.55) 0%, rgba(150,80,62,0) 100%),
      radial-gradient(ellipse 30% 12% at 38% 56%, rgba(80,82,88,0.9) 0%, rgba(80,82,88,0) 100%),
      radial-gradient(ellipse 12% 6% at 32% 51%, rgba(214,164,54,0.75) 0%, rgba(214,164,54,0) 100%),
      radial-gradient(ellipse 10% 6% at 55% 51%, rgba(214,164,54,0.7) 0%, rgba(214,164,54,0) 100%),
      radial-gradient(ellipse 10% 30% at 4% 45%, rgba(60,62,66,0.7) 0%, rgba(60,62,66,0) 100%),
      linear-gradient(180deg, #eceae6 0%, #e4e2de 45%, #b9b3aa 62%, #b88e5e 82%, #c79b68 100%);
  }
  .photo--unit706 {
    left: 389px; top: 252px; width: 380px; height: 242px;
    background:
      radial-gradient(ellipse 16% 20% at 23% 14%, rgba(70,130,40,0.75) 0%, rgba(70,130,40,0) 100%),
      radial-gradient(ellipse 26% 30% at 72% 45%, rgba(176,146,108,0.95) 0%, rgba(176,146,108,0) 100%),
      radial-gradient(ellipse 10% 10% at 72% 35%, rgba(40,40,40,0.45) 0%, rgba(40,40,40,0) 100%),
      radial-gradient(ellipse 10% 28% at 4% 48%, rgba(110,90,80,0.6) 0%, rgba(110,90,80,0) 100%),
      radial-gradient(ellipse 8% 8% at 37% 45%, rgba(250,250,248,0.9) 0%, rgba(250,250,248,0) 100%),
      linear-gradient(180deg, #dfe6dc 0%, #eeeeea 18%, #e8e5e0 50%, #cbb79a 72%, #c7a878 100%);
  }

  .brand-box {
    position: absolute; left: 0; top: 27px; width: 112px; height: 103px;
    background: var(--black); display: flex; align-items: center; justify-content: center;
    flex-direction: column; gap: 8px;
  }
  .brand-box__mark { width: 16px; height: 16px; background: var(--white); border-radius: 50%; }
  .brand-box__name {
    color: var(--white); font-weight: 400; font-size: 14px; line-height: 1.15; text-align: center;
  }

  .headline {
    position: absolute; left: 112px; top: 27px; width: 269px; height: 103px;
    background: linear-gradient(90deg, #dcdcdc 0%, #f4f4f4 60%, #fafafa 100%);
    padding: 10px 0 0 13px; font-weight: 700; font-size: 43px; line-height: 43px; letter-spacing: 4px;
  }
  .headline__lead { color: var(--black); display: block; }
  .headline__accent { color: var(--red); display: block; }

  .listing { position: absolute; width: 353px; }
  .listing--ours { left: 16px; top: 358px; }
  .listing--404 { left: 403px; top: 131px; }
  .listing--706 { left: 403px; top: 380px; }

  .tag-ours {
    height: 40px; width: 266px; background: var(--red); color: var(--white);
    clip-path: polygon(0 0, 170px 0, 100% 100%, 0 100%);
    display: flex; align-items: center; gap: 8px; padding-left: 11px;
  }
  .tag-ours__mark { width: 13px; height: 13px; border-radius: 50%; background: var(--white); flex: none; }
  .tag-ours__name { font-size: 13px; line-height: 1.05; font-weight: 400; }

  .tag-other {
    height: 18px; margin-left: 123px; width: 230px; background: var(--grey); color: var(--white);
    clip-path: polygon(22px 0, 100% 0, 100% 100%, 0 100%);
    font-size: 10px; font-weight: 700; letter-spacing: 1px; text-align: right; padding: 2px 4px 0 0;
  }

  .listing__address {
    height: 23px; background: var(--black); color: var(--white); text-align: center;
    font-size: 11.5px; font-weight: 700; letter-spacing: 1.5px; line-height: 23px;
  }
  .stats {
    height: 44px; background: var(--white); display: grid; grid-template-columns: 1fr 2px 1fr;
    padding: 5px 9px 3px;
  }
  .stats__col { display: flex; flex-direction: column; }
  .stats__row {
    flex: 1; display: flex; align-items: center; justify-content: center;
    font-size: 9px; font-weight: 700; letter-spacing: 1.2px; color: var(--black); white-space: nowrap;
  }
  .stats__row + .stats__row { border-top: 2px solid var(--rule); }
  .stats__col:first-child { margin-right: 9px; }
  .stats__col:last-child { margin-left: 9px; }
  .stats__sep { background: var(--rule); margin: -2px 0 3px; }
  .stats__value--hot { color: var(--red); }
  .listing__specs {
    height: 15px; background: var(--black); color: var(--white); text-align: center;
    font-size: 6.5px; font-weight: 700; letter-spacing: 0.8px; line-height: 15px;
  }
</style>
</head>
<body>
  <h1 class="sheet-title">Postcard 2 : Comparison</h1>

  <section class="postcard">
    <div class="photo photo--feature" role="img" aria-label="Bright living room with grey sofas, round glass coffee table and city view windows"></div>
    <div class="photo photo--unit404" role="img" aria-label="Living room with grey sectional sofa, yellow pillows and dining chairs"></div>
    <div class="photo photo--unit706" role="img" aria-label="Corner with tan armchair, striped throw and potted plants"></div>

    <div class="brand-box">
      <span class="brand-box__mark"></span>
      <span class="brand-box__name">MARLOW KENT<br>REALTY GROUP</span>
    </div>
    <h2 class="headline"><span class="headline__lead">LET'S</span><span class="headline__accent">COMPARE</span></h2>

    <article class="listing listing--ours">
      <div class="tag-ours"><span class="tag-ours__mark"></span><span class="tag-ours__name">MARLOW KENT<br>REALTY GROUP</span></div>
      <div class="listing__address">42 Palmer Avenue, Unit 718, Cambridge</div>
      <div class="stats">
        <div class="stats__col">
          <div class="stats__row">LIST PRICE : $1,189,000</div>
          <div class="stats__row">SALE PRICE :&nbsp;<span class="stats__value--hot">$1,300,000</span></div>
        </div>
        <div class="stats__sep"></div>
        <div class="stats__col">
          <div class="stats__row">DAYS ON MARKET : 8</div>
          <div class="stats__row">SALE TO LIST PRICE :&nbsp;<span class="stats__value--hot">109%</span></div>
        </div>
      </div>
      <div class="listing__specs">2 bedrooms, 2 bathrooms, 1327 square feet</div>
    </article>

    <article class="listing listing--404">
      <div class="tag-other">Unit Sold By Other Agents</div>
      <div class="listing__address">42 Palmer Avenue, Unit 404, Cambridge</div>
      <div class="stats">
        <div class="stats__col">
          <div class="stats__row">LIST PRICE : $1,250,000</div>
          <div class="stats__row">SALE PRICE :&nbsp;<span class="stats__value--hot">$1,200,000</span></div>
        </div>
        <div class="stats__sep"></div>
        <div class="stats__col">
          <div class="stats__row">DAYS ON MARKET :&nbsp;<span class="stats__value--hot">25</span></div>
          <div class="stats__row">SALE TO LIST PRICE :&nbsp;<span class="stats__value--hot">96%</span></div>
        </div>
      </div>
      <div class="listing__specs">2 bedroom, 2 bathroom, 1369 square feet</div>
    </article>

    <article class="listing listing--706">
      <div class="tag-other">Unit Sold By Other Agents</div>
      <div class="listing__address">42 Palmer Avenue, Unit 706, Cambridge</div>
      <div class="stats">
        <div class="stats__col">
          <div class="stats__row">LIST PRICE : $1,195,000</div>
          <div class="stats__row">SALE PRICE :&nbsp;<span class="stats__value--hot">$1,180,000</span></div>
        </div>
        <div class="stats__sep"></div>
        <div class="stats__col">
          <div class="stats__row">DAYS ON MARKET :&nbsp;<span class="stats__value--hot">74</span></div>
          <div class="stats__row">SALE TO LIST PRICE :&nbsp;<span class="stats__value--hot">99%</span></div>
        </div>
      </div>
      <div class="listing__specs">2 bedrooms, 2 bathrooms, 1277 square feet</div>
    </article>
  </section>
</body>
</html>
```